St Velor 43rd Festival

We need a poster design for the 43rd St Velor Youth Festival.
The festival will include a church service, folkloric dancing and a live band. The poster will be primarily in the Cyrillic language so it will need to be editable by us to confirm the writing.
I have attached a older design that we would like to use as a base. The new look of the poster is to be fresh and clean, i have attached an example of the new / clean poster. We would like to incorporate our countries nations colours, red, blue and white like in the example.

You will have to extract the text from the scanned 'old poster' pdf document

I have marked up a image 'my thoughts' to help

Once this poster is finalised we will engage with you further for to design menu poster, entry ticket design etc.

```html
<!DOCTYPE html>
<html lang="sr">
<head>
<meta charset="utf-8">
<title>43rd St. Velor Youth Festival</title>
<link rel="stylesheet" href="https://fonts.googleapis.com/css2?family=Oswald:wght@400;500;700&family=Roboto+Condensed:wght@400;700&display=swap">
<style>
  :root {
    --red: #d8252c;
    --blue: #1f3fa8;
    --navy: #17307f;
    --white: #ffffff;
    --stone: #d9a571;
    --stone-dark: #a86d3e;
    --sky: #8fb6e3;
  }
  * { margin: 0; padding: 0; box-sizing: border-box; }
  html, body { width: 849px; height: 1200px; overflow: hidden; background: var(--white); }
  .poster { position: relative; width: 849px; height: 1200px; overflow: hidden; font-family: "Roboto Condensed", sans-serif; }
  .backdrop { position: absolute; inset: 0; }
  .title { position: absolute; top: 36px; left: 20px; right: 20px; text-align: center; color: var(--white);
    font-family: "Oswald", sans-serif; font-weight: 500; font-size: 54px; line-height: 1; letter-spacing: 0.5px; white-space: nowrap; z-index: 2; }
  .title sup { font-size: 28px; vertical-align: 18px; font-weight: 400; }
  .subtitle { position: absolute; top: 112px; left: 20px; right: 20px; text-align: center; color: var(--white);
    font-family: "Oswald", sans-serif; font-size: 16px; letter-spacing: 0.5px; white-space: nowrap; z-index: 2; }
  .church-photo { position: absolute; top: 160px; left: 0; width: 849px; height: 400px;
    background: linear-gradient(180deg, var(--sky) 0%, #c8d9ee 30%, var(--stone) 45%, var(--stone-dark) 100%);
    -webkit-mask-image: linear-gradient(180deg, transparent 0%, #000 20%, #000 80%, transparent 100%);
    mask-image: linear-gradient(180deg, transparent 0%, #000 20%, #000 80%, transparent 100%); }
  .circle { position: absolute; border-radius: 50%; border: 6px solid var(--white); box-shadow: 0 4px 14px rgba(0,0,0,.3); }
  .circle--food { left: 14px; top: 410px; width: 230px; height: 230px; background: radial-gradient(circle, #b8573a, #6d3420 70%, #e8e2d6 100%); }
  .circle--band { left: 283px; top: 425px; width: 265px; height: 265px; background: radial-gradient(circle at 50% 60%, #2b2b33, #c9b9a0 80%); }
  .circle--folk { left: 580px; top: 395px; width: 255px; height: 255px; background: radial-gradient(circle at 50% 60%, #c23a34, #3a3f55 80%); }
  .schedule { position: absolute; left: 40px; top: 695px; width: 470px; color: var(--white); }
  .day { font-family: "Oswald", sans-serif; font-weight: 700; font-size: 27px; line-height: 1.25; margin-top: 6px; }
  .item { font-size: 15px; line-height: 1.28; padding-left: 6px; }
  .notice { position: absolute; right: 0; width: 320px; font-family: "Oswald", sans-serif; font-weight: 500; font-size: 18px; line-height: 1.2; padding: 10px 14px 10px 36px; }
  .notice--food { top: 720px; background: var(--white); color: var(--red); }
  .notice--music { top: 815px; width: 300px; background: var(--white); color: var(--blue); }
  .welcome { position: absolute; left: 40px; right: 40px; top: 1020px; color: var(--red);
    font-family: "Oswald", sans-serif; font-weight: 500; font-size: 20px; line-height: 1.3; }
  .contact { position: absolute; left: 40px; right: 40px; top: 1135px; color: var(--blue);
    font-family: "Oswald", sans-serif; font-weight: 500; font-size: 30px; white-space: nowrap; }
</style>
</head>
<body>
<main class="poster">
  <svg class="backdrop" width="849" height="1200" viewBox="0 0 849 1200" aria-hidden="true">
    <rect width="849" height="1200" fill="var(--white)"/>
    <polygon points="0,0 849,0 849,60 0,360" fill="var(--blue)"/>
    <polygon points="0,0 520,0 0,260" fill="var(--red)"/>
    <polygon points="0,640 849,600 849,700 560,1000 0,1000" fill="var(--blue)"/>
    <polygon points="0,640 849,600 849,620 0,665" fill="var(--red)"/>
  </svg>

  <div class="church-photo" role="img" aria-label="Photograph of the stone church under a blue sky"></div>

  <h1 class="title">43<sup>RD</sup> ST. VELOR YOUTH FESTIVAL</h1>
  <p class="subtitle">ЧНТРДЕСЕТ ТРЕЋИ СВЕТОВЕЛОРСКИ ОМЛАДИНСКИ ФЕСТИВАЛ</p>

  <div class="circle circle--food" role="img" aria-label="Photograph of grilled food"></div>
  <div class="circle circle--band" role="img" aria-label="Photograph of the live band"></div>
  <div class="circle circle--folk" role="img" aria-label="Photograph of the folkloric dance group"></div>

  <section class="schedule">
    <h2 class="day">ПЕТАК–26 ЈАНУАР</h2>
    <p class="item">18.00 Часова Вечерње Богослужење</p>
    <h2 class="day">СУБОТА 27.ЈАНУАР 2024</h2>
    <p class="item">10.00 Света Архијерејска Литургија</p>
    <p class="item">12.30 Отварање фестивала</p>
    <p class="item">13.00 Наступи фолклорних група и народно весеље</p>
    <p class="item">18.00 вечерње богослужење</p>
    <h2 class="day">НЕДЕЉА –28. ЈАНУАР</h2>
    <p class="item">13.00 Наступи фолклорних група и народно весеље</p>
    <p class="item">10.00 Света Литургија</p>
    <p class="item">11.30 Наставак фолклорних група</p>
    <p class="item">16.00 завршетак фестивала</p>
  </section>

  <p class="notice notice--food">ЧЕКА ВАС ДОМАТИНСКА<br>КУХИЊА И ПРИЈАТНА</p>
  <p class="notice notice--music">СРПСКА<br>МУЗИКА</p>

  <p class="welcome">ДОБРО НАМ ДОШЛИ У СВЕТОВЕЛОРСКУ СВЕТИЊУ СВИХ ВЕРНИХ СРБА АУСТРАЛИЈЕ И НОВОГ ЗЕЛАНДА, И НА ПОКЛОНЕ НЕДАВНО ПРИСТИГЛОЈ ИЗ МАНАСТИРА ВЕЛОРАНА СВЕТОЈ ИКОНИ БОГОРОДИЦИ ТРОЈЕРУЧИЦИ</p>
  <p class="contact">ЗА СВЕ ИНФОРМАЦИЈАВИТЕ СЕ НА ТЕЛ : 0400 123 456</p>
</main>
</body>
</html>
```